OTT TV and VOD Service Website (like Kestrova.tv ; Vexo etc.)

Site will be used as a marketing page integrated with subscription processing (Quandle). Looking for someone with solid experience in designing video content driven sites. For the looks; clean, modern, black background with rich "popping" VOD and live TV channel titles.

Video-on-demand and international live TV channel subscribers in Asia

Coded - Design and coding required

5+ page

• See files

Requirements
Must have
• Start with an awesome looking "coming soon" page, featuring a logo on black background with video (i.e. a movie trailers) playing in the background. This page should also have an understated "about" link and an email "contact" form.
Site: Scrollable interfaces: Service / Live Channels / VOD / Subscribe.
Contrasting backgrounds as the page is being scrolled. Black as a dominating background color. See Kestrova.tv site for inspiration
There will be contact form (Register)
Nice to have
• Dynamic video background on the home page (trailer / title / channel promo)
Clear interface separation between live TV channels and VOD
Should not have
• Typical template looking scrolling site with boring icons and

```html
<!DOCTYPE html>
<html lang="en">
<head>
<meta charset="utf-8">
<title>Lumora.tv — International Live TV Channel</title>
<link rel="stylesheet" href="https://fonts.googleapis.com/css2?family=Open+Sans:wght@400;600;700;800&display=swap">
<style>
:root{
  --bg:#131417;
  --bg-alt:#1c1d21;
  --bg-band:#25262b;
  --card:#0f1012;
  --text:#ffffff;
  --muted:#9a9ca3;
  --accent-a:#2fc48a;
  --accent-b:#1ea6d8;
  --line:#2c2d33;
}
*{box-sizing:border-box;margin:0;padding:0}
html,body{width:1200px;height:3592px;overflow:hidden}
body{background:var(--bg);color:var(--text);font-family:"Open Sans",Arial,sans-serif;position:relative}
.btn{display:inline-block;background:linear-gradient(90deg,var(--accent-a),var(--accent-b));color:#fff;font-weight:700;font-size:13px;letter-spacing:.5px;text-transform:uppercase;padding:11px 22px;border-radius:3px}
.section-title{font-size:36px;font-weight:600;text-align:center}

/* nav */
.site-nav{position:absolute;top:0;left:0;width:1200px;height:48px;display:flex;align-items:center;padding:0 40px;z-index:3;background:rgba(10,10,12,.55)}
.brand{font-size:26px;font-weight:700;display:flex;align-items:center;gap:8px}
.brand-dot{width:12px;height:12px;border-radius:50%;background:var(--accent-a)}
.nav-links{margin-left:auto;display:flex;gap:34px;font-size:13px;align-items:center}
.nav-links .btn{padding:6px 18px;font-size:12px;text-transform:none}

/* hero */
.hero{position:absolute;top:0;left:0;width:1200px;height:572px;background:radial-gradient(ellipse at 50% 55%,#3a3a40 0%,#1a1b1f 60%,#0c0c0e 100%)}
.hero-content{position:absolute;top:270px;width:100%;text-align:center}
.hero h1{font-size:46px;font-weight:700;margin-bottom:30px}
.hero-dots{position:absolute;top:516px;width:100%;display:flex;justify-content:center;gap:10px}
.hero-dots span{width:8px;height:8px;border-radius:50%;background:#777}
.hero-dots span:first-child{background:#fff}

/* feature grid */
.feature-grid{position:absolute;top:572px;left:0;width:1200px;height:468px}
.tile{position:absolute;overflow:hidden}
.tile-label{position:absolute;left:18px;bottom:18px}
.tile-label small{display:block;font-size:10px;color:#ddd;text-transform:uppercase}
.tile-label strong{font-size:24px;font-weight:600}
.tile-label em{display:block;font-style:normal;font-size:10px;color:#ccc}

/* carousels */
.carousel{position:absolute;left:0;width:1200px}
.row{display:flex;gap:12px;justify-content:center}
.arrow{position:absolute;width:26px;height:44px;background:#d8d8d8;display:flex;align-items:center;justify-content:center}
.arrow svg{width:12px;height:12px}
.thumb{position:relative;border-radius:4px}
.live-badge{position:absolute;top:8px;left:8px;background:var(--accent-a);font-size:9px;font-weight:700;padding:2px 6px;border-radius:2px}

/* tv band */
.tv-band{position:absolute;top:1288px;left:0;width:1200px;height:344px;background:linear-gradient(180deg,#2a2b30 0%,#1e1f23 100%)}
.tv-copy{position:absolute;left:92px;top:104px;width:360px}
.tv-copy h2{font-size:34px;font-weight:600;margin-bottom:10px}
.tv-copy p{font-size:12px;color:var(--muted);line-height:1.5;margin-bottom:22px}
.tv-screen{position:absolute;left:592px;top:44px;width:496px;height:250px;border-radius:4px;background:linear-gradient(135deg,#2b4b7a,#6a2f5c 50%,#d08a3a)}

/* movies */
.poster-caption{margin-top:10px}
.poster-caption strong{display:block;font-size:14px;font-weight:600}
.poster-caption span{font-size:11px;color:var(--muted)}
.divider{position:absolute;top:2092px;left:80px;width:1040px;height:1px;background:var(--line)}
.vod-caption{position:absolute;left:14px;bottom:12px;display:flex;gap:8px;align-items:center}
.play{width:22px;height:22px;border-radius:50%;background:rgba(255,255,255,.9);display:flex;align-items:center;justify-content:center}
.vod-caption strong{display:block;font-size:12px}
.vod-caption span{font-size:10px;color:#ccc}

/* plans */
.plans{position:absolute;top:2380px;left:0;width:1200px;height:660px;background:var(--bg-band)}
.plans .section-title{margin-top:46px}
.plan-cards{position:absolute;top:124px;left:160px;display:flex;gap:32px}
.plan{width:272px;height:464px;background:var(--card);border-radius:6px;text-align:center;padding-top:26px}
.plan h3{font-size:20px;font-weight:700;text-transform:uppercase}
.plan .sub{font-size:13px;color:#ccc;margin:6px 0 16px}
.price{display:inline-flex;align-items:center;background:#fff;color:#111;border-radius:16px;padding:3px 14px 3px 3px;font-size:13px;font-weight:600;gap:8px}
.price b{background:var(--accent-a);color:#fff;border-radius:50%;width:26px;height:26px;display:flex;align-items:center;justify-content:center}
.plan ul{list-style:none;text-align:left;margin:30px 26px 28px;font-size:11px;color:var(--muted);line-height:1.5}
.plan li{display:flex;gap:8px;margin-bottom:14px}
.plan li svg{flex:none;width:12px;height:12px;margin-top:2px}

/* cta */
.cta{position:absolute;top:3040px;left:0;width:1200px;height:160px;background:var(--bg-alt);display:flex;align-items:center;justify-content:center;gap:34px}
.cta h2{font-size:34px;font-weight:400}
.cta h2 b{font-weight:700}

/* footer */
.site-footer{position:absolute;top:3200px;left:0;width:1200px;height:392px;background:#0e0f11}
.site-footer .brand{position:absolute;left:100px;top:84px;font-size:44px}
.social{position:absolute;left:100px;top:196px;display:flex;gap:16px}
.social span{width:16px;height:16px;border-radius:50%;background:#fff}
.stores{position:absolute;left:100px;top:296px;display:flex;gap:12px}
.stores span{width:110px;height:34px;border-radius:5px;background:#2a2b30;border:1px solid #555}
.foot-cols{position:absolute;left:480px;top:76px;display:flex;gap:80px;font-size:12px;color:var(--muted);line-height:2.1}
.copy{position:absolute;right:100px;top:350px;font-size:11px;color:var(--muted)}
</style>
</head>
<body>

<section class="hero">
  <div role="img" aria-label="Wall of television screens showing channel programmes" style="position:absolute;inset:0;background:linear-gradient(180deg,rgba(70,70,80,.5),rgba(20,20,24,.2) 60%,rgba(10,10,12,.8))"></div>
  <div class="hero-content">
    <h1>International Live TV Channel</h1>
    <span class="btn">Subscribe Now</span>
  </div>
  <div class="hero-dots"><span></span><span></span><span></span><span></span><span></span></div>
</section>

<nav class="site-nav">
  <div class="brand"><span class="brand-dot"></span>Lumora.tv</div>
  <div class="nav-links"><span>Home</span><span>Service</span><span>Live Channels</span><span>Pricing Plan</span><span>About Us</span><span class="btn">Login</span></div>
</nav>

<section class="feature-grid">
  <div class="tile" role="img" aria-label="Performer on stage at an outdoor concert" style="left:0;top:0;width:400px;height:468px;background:linear-gradient(160deg,#6f8f5a,#3f5a33 55%,#2a2a2a)">
    <div class="tile-label"><small>Live concert</small><strong>Pellentesque</strong><em>Music, Show</em></div>
  </div>
  <div class="tile" role="img" aria-label="Animated film key art" style="left:400px;top:0;width:392px;height:236px;background:linear-gradient(135deg,#c33a2a,#e6a53a 50%,#3b5ea8)">
    <div class="tile-label"><small>Family</small><strong>Sollicitudin</strong><em>Animation, Comedy</em></div>
  </div>
  <div class="tile" role="img" aria-label="City street scene at night" style="left:400px;top:236px;width:392px;height:232px;background:linear-gradient(135deg,#2a1420,#8a2a3a 55%,#1c1c28)">
    <div class="tile-label"><small>Drama</small><strong>Imperdiet</strong><em>Crime, Thriller</em></div>
  </div>
  <div class="tile" role="img" aria-label="Dancer lit by neon lights" style="left:792px;top:0;width:408px;height:468px;background:linear-gradient(160deg,#0f6b5e,#1fb39a 45%,#2a1a2e)">
    <div class="tile-label"><small>Music</small><strong>Pellentesque</strong><em>Dance, Show</em></div>
  </div>
</section>

<h2 class="section-title" style="position:absolute;top:1050px;width:1200px;font-size:32px">Live Channels</h2>
<div class="carousel" style="top:1112px">
  <div class="arrow" style="left:80px;top:42px"><svg viewBox="0 0 12 12"><path d="M8 1 3 6l5 5" stroke="#333" stroke-width="2" fill="none"/></svg></div>
  <div class="row">
    <div class="thumb" role="img" aria-label="Live talk show stage" style="width:196px;height:128px;background:linear-gradient(135deg,#3a2a24,#7a5a3a)"><span class="live-badge">LIVE</span></div>
    <div class="thumb" role="img" aria-label="Stadium football match" style="width:196px;height:128px;background:linear-gradient(135deg,#1d3a22,#4f8a45)"><span class="live-badge">LIVE</span></div>
    <div class="thumb" role="img" aria-label="Concert crowd under stage lights" style="width:196px;height:128px;background:linear-gradient(135deg,#3a1050,#c23a8a)"><span class="live-badge">LIVE</span></div>
    <div class="thumb" role="img" aria-label="Mountain landscape documentary" style="width:196px;height:128px;background:linear-gradient(135deg,#6a7f93,#c7ccd2)"><span class="live-badge">LIVE</span></div>
    <div class="thumb" role="img" aria-label="Singer performing on stage" style="width:196px;height:128px;background:linear-gradient(135deg,#1a1a1c,#5a4a40)"><span class="live-badge">LIVE</span></div>
  </div>
  <div class="arrow" style="right:80px;top:42px"><svg viewBox="0 0 12 12"><path d="M4 1l5 5-5 5" stroke="#333" stroke-width="2" fill="none"/></svg></div>
</div>

<section class="tv-band">
  <div class="tv-copy">
    <h2>Enjoy Your TV Shows</h2>
    <p>Aenean tempus pellentesque, vivamus ut nisi quam phasellus sed tempus lorem nulla facilisi.</p>
    <span class="btn">Try It Now</span>
  </div>
  <div class="tv-screen" role="img" aria-label="Television set displaying a grid of shows"></div>
  <div style="position:absolute;left:560px;top:294px;width:560px;height:6px;background:#0c0c0e;border-radius:2px"></div>
</section>

<h2 class="section-title" style="position:absolute;top:1680px;width:1200px">Popular Movies</h2>
<div class="carousel" style="top:1744px">
  <div class="arrow" style="left:80px;top:102px"><svg viewBox="0 0 12 12"><path d="M8 1 3 6l5 5" stroke="#333" stroke-width="2" fill="none"/></svg></div>
  <div class="row" style="gap:16px">
    <div><div class="thumb" role="img" aria-label="Movie poster, dark portrait" style="width:188px;height:248px;background:linear-gradient(160deg,#3a3a3e,#121214)"></div><div class="poster-caption"><strong>Lorem Ipsum</strong><span>Adventure, Drama</span></div></div>
    <div><div class="thumb" role="img" aria-label="Movie poster with neon lights" style="width:188px;height:248px;background:linear-gradient(160deg,#6a1a8a,#d23a6a)"></div><div class="poster-caption"><strong>Lorem Ipsum</strong><span>Adventure, Drama</span></div></div>
    <div><div class="thumb" role="img" aria-label="Movie poster, warriors in a desert" style="width:188px;height:248px;background:linear-gradient(160deg,#b8a078,#5a4a38)"></div><div class="poster-caption"><strong>Lorem Ipsum</strong><span>Adventure, Drama</span></div></div>
    <div><div class="thumb" role="img" aria-label="Movie poster, horror figure" style="width:188px;height:248px;background:linear-gradient(160deg,#4a4a3a,#141412)"></div><div class="poster-caption"><strong>Lorem Ipsum</strong><span>Adventure, Drama</span></div></div>
    <div><div class="thumb" role="img" aria-label="Movie poster, costumed hero" style="width:188px;height:248px;background:linear-gradient(160deg,#c24a2a,#3a2a2a)"></div><div class="poster-caption"><strong>Lorem Ipsum</strong><span>Adventure, Drama</span></div></div>
  </div>
  <div class="arrow" style="right:80px;top:102px"><svg viewBox="0 0 12 12"><path d="M4 1l5 5-5 5" stroke="#333" stroke-width="2" fill="none"/></svg></div>
</div>

<div class="divider"></div>

<h2 class="section-title" style="position:absolute;top:2112px;width:1200px;font-size:32px">Video On Demand</h2>
<div class="carousel" style="top:2168px">
  <div class="arrow" style="left:80px;top:60px"><svg viewBox="0 0 12 12"><path d="M8 1 3 6l5 5" stroke="#333" stroke-width="2" fill="none"/></svg></div>
  <div class="row" style="gap:16px">
    <div class="thumb" role="img" aria-label="Dancer on a dark stage" style="width:240px;height:164px;background:linear-gradient(135deg,#0e0e10,#4a3a3a)"><div class="vod-caption"><span class="play"><svg width="9" height="9" viewBox="0 0 10 10"><path d="M2 1l7 4-7 4z" fill="#222"/></svg></span><div><strong>Quisque malesuada</strong><span>Romance, Drama</span></div></div></div>
    <div class="thumb" role="img" aria-label="Nature documentary scene" style="width:240px;height:164px;background:linear-gradient(135deg,#2a5a6a,#7aa06a)"><div class="vod-caption"><span class="play"><svg width="9" height="9" viewBox="0 0 10 10"><path d="M2 1l7 4-7 4z" fill="#222"/></svg></span><div><strong>Quisque malesuada</strong><span>Romance, Drama</span></div></div></div>
    <div class="thumb" role="img" aria-label="Fashion show under bright lights" style="width:240px;height:164px;background:linear-gradient(135deg,#3a2a1a,#c0883a)"><div class="vod-caption"><span class="play"><svg width="9" height="9" viewBox="0 0 10 10"><path d="M2 1l7 4-7 4z" fill="#222"/></svg></span><div><strong>Quisque malesuada</strong><span>Romance, Drama</span></div></div></div>
    <div class="thumb" role="img" aria-label="Outdoor drama in a green field" style="width:240px;height:164px;background:linear-gradient(135deg,#6a7a4a,#b0b890)"><div class="vod-caption"><span class="play"><svg width="9" height="9" viewBox="0 0 10 10"><path d="M2 1l7 4-7 4z" fill="#222"/></svg></span><div><strong>Quisque malesuada</strong><span>Romance, Drama</span></div></div></div>
  </div>
  <div class="arrow" style="right:80px;top:60px"><svg viewBox="0 0 12 12"><path d="M4 1l5 5-5 5" stroke="#333" stroke-width="2" fill="none"/></svg></div>
</div>

<section class="plans">
  <h2 class="section-title">Select Your Plan</h2>
  <div class="plan-cards">
    <div class="plan">
      <h3>Quisque Malesuada</h3><p class="sub">Get 1 month free, then starts at</p>
      <span class="price"><b>$</b>5.00 /month</span>
      <ul>
        <li><svg viewBox="0 0 12 12"><path d="M1 6l3 3 7-7" stroke="#2fc48a" stroke-width="2" fill="none"/></svg>Nunc feugiat nulla sed nisl pellentesque, quisque tempus vestibulum lorem.</li>
        <li><svg viewBox="0 0 12 12"><path d="M1 6l3 3 7-7" stroke="#2fc48a" stroke-width="2" fill="none"/></svg>Orci varius natoque penatibus et magnis dis parturient montes.</li>
        <li><svg viewBox="0 0 12 12"><path d="M1 6l3 3 7-7" stroke="#2fc48a" stroke-width="2" fill="none"/></svg>Mauris egestas scelerisque vestibulum, quisque lacinia ante risus.</li>
        <li><svg viewBox="0 0 12 12"><path d="M1 6l3 3 7-7" stroke="#2fc48a" stroke-width="2" fill="none"/></svg>Praesent ultrices purus tellus, pellentesque vitae finibus lorem.</li>
      </ul>
      <span class="btn">Buy Now</span>
    </div>
    <div class="plan">
      <h3>Quisque Malesuada</h3><p class="sub">Get 1 month free, then starts at</p>
      <span class="price"><b>$</b>8.25 /month</span>
      <ul>
        <li><svg viewBox="0 0 12 12"><path d="M1 6l3 3 7-7" stroke="#2fc48a" stroke-width="2" fill="none"/></svg>Nunc feugiat nulla sed nisl pellentesque, quisque tempus vestibulum lorem.</li>
        <li><svg viewBox="0 0 12 12"><path d="M1 6l3 3 7-7" stroke="#2fc48a" stroke-width="2" fill="none"/></svg>Orci varius natoque penatibus et magnis dis parturient montes.</li>
        <li><svg viewBox="0 0 12 12"><path d="M1 6l3 3 7-7" stroke="#2fc48a" stroke-width="2" fill="none"/></svg>Mauris egestas scelerisque vestibulum, quisque lacinia ante risus.</li>
        <li><svg viewBox="0 0 12 12"><path d="M1 6l3 3 7-7" stroke="#2fc48a" stroke-width="2" fill="none"/></svg>Praesent ultrices purus tellus, pellentesque vitae finibus lorem.</li>
      </ul>
      <span class="btn">Buy Now</span>
    </div>
    <div class="plan">
      <h3>Quisque Malesuada</h3><p class="sub">Get 1 month free, then starts at</p>
      <span class="price"><b>$</b>12.50 /month</span>
      <ul>
        <li><svg viewBox="0 0 12 12"><path d="M1 6l3 3 7-7" stroke="#2fc48a" stroke-width="2" fill="none"/></svg>Nunc feugiat nulla sed nisl pellentesque, quisque tempus vestibulum lorem.</li>
        <li><svg viewBox="0 0 12 12"><path d="M1 6l3 3 7-7" stroke="#2fc48a" stroke-width="2" fill="none"/></svg>Orci varius natoque penatibus et magnis dis parturient montes.</li>
        <li><svg viewBox="0 0 12 12"><path d="M1 6l3 3 7-7" stroke="#2fc48a" stroke-width="2" fill="none"/></svg>Mauris egestas scelerisque vestibulum, quisque lacinia ante risus.</li>
        <li><svg viewBox="0 0 12 12"><path d="M1 6l3 3 7-7" stroke="#2fc48a" stroke-width="2" fill="none"/></svg>Praesent ultrices purus tellus, pellentesque vitae finibus lorem.</li>
      </ul>
      <span class="btn">Buy Now</span>
    </div>
  </div>
</section>

<section class="cta">
  <h2>Watch Thousands of <b>Shows</b> and <b>Movies</b></h2>
  <span class="btn">Subscribe Now</span>
</section>

<footer class="site-footer">
  <div class="brand"><span class="brand-dot" style="width:18px;height:18px"></span>Lumora.tv</div>
  <div class="social"><span></span><span></span><span></span><span></span></div>
  <div class="stores"><span></span><span></span></div>
  <div class="foot-cols">
    <div>Streaming Shows<br>Live TV<br>Live News<br>Live Sports</div>
    <div>TV Shows<br>Movies<br>Originals<br>Networks<br>Kids</div>
    <div>Help Center<br>Jobs<br>Cookie Preferences<br>Privacy Policy<br>Terms of Use</div>
    <div>Home<br>Service<br>Live Channels<br>Pricing Plan<br>About Us</div>
  </div>
  <p class="copy">© 2024 Lumora.tv. All Rights Reserved.</p>
</footer>

</body>
</html>
```